Satchel & Compass needs new business card design

I need a new business card design. I'm looking for out-of-the-box design which represents the freedom of being a location independent entrepreneur.
I offer coaching, retreats and trips.
I would like to see designs with and without the photo.
Colors I use are black (#000000), green (#25A796) and brown (#D7C38C)
Website satchelandcompass.com

Target Market(s)

location independent entrepreneurs, digital nomads, people looking to swap the 9 to 5 for a lifestyle business

Industry/Entity Type

Business

Contact Information for Business Card

Petra Varga
Your Lifestyle Business Coach, Retreat & Trip Leader
http://satchelandcompass.com
hello@satchelandcompass.com
Live a life you don't need a holiday from

Font styles to use
Serif
Sans Serif

Requirements
Must have
• One side should contain only the logo. I would also consider having the "Live a life you don't need a holiday from" on that side too (depending on how it looks)
• Please show both sides on the designs.

```html
<!DOCTYPE html>
<html lang="en">
<head>
<meta charset="utf-8">
<title>Satchel &amp; Compass – Business Card</title>
<link rel="stylesheet" href="https://fonts.googleapis.com/css2?family=Arimo:ital,wght@0,400;0,700;1,700&family=Open+Sans:wght@400;600&display=swap">
<style>
  :root {
    --bg: #7a7a78;
    --card-white: #ffffff;
    --card-dark: #2b2624;
    --teal: #25a796;
    --teal-dark: #2f4a47;
    --tan: #d7c38c;
    --ink: #3a3a3a;
    --ink-soft: #222222;
    --white: #ffffff;
  }
  * { box-sizing: border-box; margin: 0; padding: 0; }
  html, body { width: 1200px; height: 676px; overflow: hidden; }
  body {
    background: var(--bg);
    display: flex;
    align-items: center;
    justify-content: center;
    gap: 40px;
    font-family: "Open Sans", Arial, sans-serif;
  }
  .card {
    position: relative;
    width: 540px;
    height: 309px;
    overflow: hidden;
    box-shadow: 0 6px 18px rgba(0,0,0,0.25);
  }

  /* Back side */
  .card--back { background: var(--card-dark); color: var(--white); }
  .card--back .dash {
    position: absolute; left: 0; right: 0; height: 4px;
    background: repeating-linear-gradient(90deg, var(--tan) 0 34px, transparent 34px 58px);
  }
  .card--back .dash--top { top: 22px; }
  .card--back .dash--bottom { bottom: 22px; }
  .back-name {
    position: absolute; left: 0; right: 0; top: 108px; text-align: center;
    font-family: "Arimo", Arial, sans-serif; font-weight: 700; font-size: 46px;
  }
  .back-title {
    position: absolute; left: 0; right: 0; top: 170px; text-align: center;
    font-family: "Arimo", Arial, sans-serif; font-weight: 700; font-style: italic; font-size: 13px;
  }

  /* Front side */
  .card--front { background: var(--card-white); }
  .band { position: absolute; left: 0; right: 0; }
  .band--top-line { top: 0; height: 3px; background: var(--teal-dark); }
  .band--top { top: 3px; height: 8px; background: var(--teal); }
  .band--bottom { bottom: 10px; height: 11px; background: var(--teal); }
  .band--bottom-line { bottom: 3px; height: 3px; background: var(--teal-dark); }

  .brand {
    position: absolute; left: 18px; top: 26px;
    font-family: "Open Sans", Arial, sans-serif; font-weight: 600;
    font-size: 13px; color: var(--ink-soft); letter-spacing: 0.5px;
  }
  .name {
    position: absolute; right: 26px; top: 50px;
    font-family: "Arimo", Arial, sans-serif; font-weight: 700;
    font-size: 50px; color: var(--ink); letter-spacing: 0.5px;
  }
  .role {
    position: absolute; right: 26px; top: 114px;
    font-family: "Arimo", Arial, sans-serif; font-weight: 700; font-style: italic;
    font-size: 12px; color: var(--ink-soft);
  }
  .contact {
    position: absolute; left: 18px; top: 172px; list-style: none;
    font-size: 18px; line-height: 25px; color: var(--ink-soft);
  }
  .contact li { display: flex; align-items: center; gap: 8px; }
  .contact svg { width: 17px; height: 17px; flex: none; }
  .tagline { padding-left: 0; }
</style>
</head>
<body>
  <section class="card card--back" aria-label="Business card, back">
    <div class="dash dash--top"></div>
    <h2 class="back-name">Petra Varga</h2>
    <p class="back-title">Your Lifestyle Business Coach, Retreat &amp; Trip Leader</p>
    <div class="dash dash--bottom"></div>
  </section>

  <section class="card card--front" aria-label="Business card, front">
    <div class="band band--top-line"></div>
    <div class="band band--top"></div>
    <p class="brand">Satchel &amp; Compass</p>
    <h1 class="name">Petra Varga</h1>
    <p class="role">Your Lifestyle Business Coach, Retreat &amp; Trip Leader</p>
    <ul class="contact">
      <li>
        <svg viewBox="0 0 20 20" aria-hidden="true">
          <circle cx="10" cy="10" r="9" fill="#222"/>
          <path d="M5 6c2 0 3 1 3 3s-2 2-2 4l-1 2M12 3c0 2 2 3 4 3M13 11c2 0 3 1 2 4" stroke="#fff" stroke-width="1.4" fill="none"/>
        </svg>
        <span>http://satchelandcompass.com</span>
      </li>
      <li>
        <svg viewBox="0 0 20 20" aria-hidden="true">
          <rect x="1.5" y="4" width="17" height="12" fill="none" stroke="#222" stroke-width="1.6"/>
          <path d="M1.5 4l8.5 7 8.5-7" fill="none" stroke="#222" stroke-width="1.6"/>
        </svg>
        <span>hello@satchelandcompass.com</span>
      </li>
      <li class="tagline">Live a life you don't need a holiday from</li>
    </ul>
    <div class="band band--bottom"></div>
    <div class="band band--bottom-line"></div>
  </section>
</body>
</html>
```